80's Band Poster

I'm looking for help. My wife's name is Marla and both my and my son's name are Toby. She signs all our mail with "Marla and the Tobys." I think it would be an amazing Christmas present to get an 80's themed band poster for her as if she was the lead singer of the band Marla and the Tobys. Lots of angular pinks and teals? Maybe just a logo/design. I don't know. I'd love to see some ideas. Let me know if you have any questions. I can provide pictures if you think you's like to include them in your design/illustration.

Requirements
Must have
• Fun. Excitement. 80's

```html
<!DOCTYPE html>
<html lang="en">
<head>
<meta charset="utf-8">
<title>Hard Times – Marla and the Tobys</title>
<link rel="stylesheet" href="https://fonts.googleapis.com/css2?family=Poppins:wght@500&family=Bevan&family=Raleway:wght@400;500&family=Montserrat:wght@500&display=swap">
<style>
  :root {
    --lilac: #df9ff5;
    --teal: #7ff5e0;
    --sky: #2f9fe6;
    --magenta: #dc37a8;
    --lemon: #fbf36b;
    --ink: #101014;
    --plum: #2a1231;
    --white: #ffffff;
    --amber: #eec44c;
    --coral: #f4644a;
    --cyan: #4fd0f5;
  }
  * { margin: 0; padding: 0; box-sizing: border-box; }
  html, body { width: 849px; height: 1200px; overflow: hidden; background: var(--lilac); }
  .poster { position: relative; width: 849px; height: 1200px; background: var(--lilac); overflow: hidden; }
  .shapes { position: absolute; inset: 0; }

  .presenter {
    position: absolute; left: 314px; top: 110px;
    font-family: "Montserrat", sans-serif; font-weight: 500;
    font-size: 18px; letter-spacing: 5px; color: var(--ink); white-space: nowrap;
    transform: rotate(-8deg); transform-origin: left center;
  }

  .title {
    position: absolute; left: 158px; top: 162px;
    font-family: "Poppins", sans-serif; font-weight: 500;
    font-size: 206px; line-height: 186px; color: var(--teal);
    -webkit-text-stroke: 5px var(--ink); paint-order: stroke fill;
    text-shadow: 7px 7px 0 var(--ink), 12px 4px 0 var(--lemon), 12px 12px 0 var(--lemon);
    transform: rotate(-8deg); transform-origin: left top;
    letter-spacing: -2px; white-space: nowrap;
  }
  .title span { display: block; }
  .title .line-two { margin-left: -4px; }

  .boombox {
    position: absolute; left: 232px; top: 560px; width: 440px; height: 290px;
    background: linear-gradient(180deg, var(--teal) 0 22%, var(--amber) 22% 88%, var(--coral) 88%);
    border: 4px solid var(--plum);
    transform: rotate(-5deg);
  }

  .billing { position: absolute; left: 0; width: 849px; text-align: center; white-space: nowrap; }
  .billing-intro {
    top: 900px; font-family: "Raleway", sans-serif; font-weight: 400;
    font-size: 18px; letter-spacing: 3.5px; color: var(--lemon);
  }
  .billing-act {
    top: 934px; font-family: "Bevan", serif; font-size: 38px;
    letter-spacing: 0.5px; color: var(--plum);
  }

  .rule { position: absolute; left: 188px; width: 472px; height: 1.5px; background: var(--white); opacity: .9; }
  .rule.top { top: 994px; }
  .rule.bottom { top: 1102px; }

  .date-badge { position: absolute; left: 198px; top: 1006px; width: 136px; height: 80px; }
  .date-badge .date {
    height: 50px; background: var(--cyan); color: var(--white);
    font-family: "Raleway", sans-serif; font-weight: 500; font-size: 27px;
    display: flex; align-items: center; justify-content: center;
  }
  .date-badge .doors {
    height: 30px; background: var(--lemon); color: var(--magenta);
    font-family: "Raleway", sans-serif; font-size: 9px;
    display: flex; align-items: center; justify-content: center;
  }

  .venue { position: absolute; left: 354px; top: 1010px; font-family: "Raleway", sans-serif; white-space: nowrap; }
  .venue-name { font-size: 39px; font-weight: 400; color: var(--white); line-height: 44px; letter-spacing: 1px; }
  .venue-address { font-size: 18px; color: var(--lemon); letter-spacing: 0.6px; margin-top: 6px; }

  .website {
    position: absolute; top: 1114px; left: 0; width: 849px; text-align: center;
    font-family: "Raleway", sans-serif; font-size: 19px; letter-spacing: 3px; color: var(--white);
  }
</style>
</head>
<body>
<main class="poster">
  <svg class="shapes" width="849" height="1200" viewBox="0 0 849 1200" aria-hidden="true">
    <polygon points="290,106 210,346 732,392" fill="var(--sky)"/>
    <polygon points="172,90 200,150 152,118" fill="var(--magenta)"/>
    <polygon points="700,118 738,134 712,166" fill="var(--lemon)"/>
    <polygon points="106,254 162,254 106,320" fill="var(--lemon)"/>
    <polygon points="712,436 752,458 730,486" fill="var(--magenta)"/>
    <polygon points="56,660 174,636 106,720" fill="var(--magenta)"/>
    <polygon points="672,700 768,690 768,808" fill="var(--lemon)"/>
    <polygon points="84,1020 120,1002 116,1070" fill="var(--lemon)"/>
    <polygon points="712,1000 770,988 762,1038" fill="var(--sky)"/>
    <g fill="none" stroke="var(--white)" stroke-width="3">
      <polyline points="100,406 112,394 120,404 132,392 140,402 150,392"/>
      <polyline points="716,318 728,306 736,316 746,306"/>
      <polyline points="728,644 740,656 748,646 760,660 768,650 776,666"/>
      <polyline points="106,832 120,816 128,828 142,812 150,822 168,808"/>
    </g>
    <g fill="var(--plum)">
      <ellipse cx="100" cy="538" rx="24" ry="8" transform="rotate(35 100 538)"/>
      <ellipse cx="732" cy="572" rx="26" ry="8" transform="rotate(10 732 572)"/>
      <ellipse cx="176" cy="876" rx="24" ry="8" transform="rotate(-50 176 876)"/>
    </g>
  </svg>

  <div class="presenter">YOUR PRESENTS</div>

  <h1 class="title"><span class="line-one">HARD</span><span class="line-two">TIMES</span></h1>

  <div class="boombox" role="img" aria-label="Illustration of a retro teal and yellow boombox with pink speakers"></div>

  <p class="billing billing-intro">SPECIAL PERFORMACES BY</p>
  <p class="billing billing-act">MARLA AND THE TOBYS</p>

  <div class="rule top"></div>

  <div class="date-badge">
    <div class="date">02.03.16</div>
    <div class="doors">DOORS OPEN AT 9:00 PM</div>
  </div>

  <div class="venue">
    <div class="venue-name">NEONWAVE CLUB</div>
    <div class="venue-address">2480 ARCADE AVENUE NEW YORK 40112</div>
  </div>

  <div class="rule bottom"></div>

  <p class="website">WWW.NEONWAVECLUB.COM</p>
</main>
</body>
</html>
```